Design a poster that illustrates the six central pillars of our school district's efforts with students. The attached PDF outlines the six main competencies we aim for students to possess upon graduation. Each of the 6 has 3 bullet points for the poster as well. The title is "Profile of a Drifter". Our mascot is this attached winged wheel. The overall concept is that staff take kids when they are young and develop these 6 things when they graduate. Our colors are navy, red, and white. We will make this poster in a variety of sizes in offices, classrooms, and in digital spaces as well. On the PDF - ignore the column that says "Synthesis". That has nothing to do with this poster.

The district is Corvath Falls Public Schools https://www.corvath.k12.example.us/

```html
<!DOCTYPE html>
<html lang="en">
<head>
<meta charset="utf-8">
<title>Profile of a Drifter</title>
<link href="https://fonts.googleapis.com/css2?family=Oswald:wght@700&family=Red+Hat+Text:wght@500;700&display=swap" rel="stylesheet">
<style>
  :root {
    --navy: #0e0f3d;
    --red: #9c1c24;
    --white: #ffffff;
    --ink: #111111;
    --rule: #111111;
  }
  * { box-sizing: border-box; margin: 0; padding: 0; }
  html, body { width: 950px; height: 1200px; overflow: hidden; background: var(--white); }
  body { font-family: "Red Hat Text", Arial, sans-serif; color: var(--ink); }

  .poster { width: 950px; height: 1200px; display: flex; flex-direction: column; }
  .poster-main { position: relative; height: 1118px; background: var(--navy); }

  .poster-title {
    position: absolute; left: 53px; top: 44px;
    font-family: "Oswald", "Arial Narrow", sans-serif; font-weight: 700;
    font-size: 58px; line-height: 1; letter-spacing: 0.5px;
    color: var(--white); text-transform: uppercase;
  }

  .district-mark {
    position: absolute; right: 56px; top: 58px;
    display: flex; align-items: center; gap: 10px;
    font-weight: 700; font-size: 22px; color: var(--white);
  }
  .district-mark .dot { width: 26px; height: 26px; border-radius: 50%; background: var(--red); }

  .competency-table {
    position: absolute; left: 57px; top: 132px; width: 836px;
    border: 2px solid var(--rule); background: var(--white);
    border-collapse: collapse;
  }
  .competency-table th, .competency-table td { border: 2px solid var(--rule); }
  .table-caption th {
    height: 52px; text-align: center; color: var(--red);
    font-family: "Oswald", sans-serif; font-weight: 700; font-size: 26px;
    text-transform: uppercase; letter-spacing: 0.2px;
  }
  .col-heads th {
    height: 45px; background: var(--red); color: var(--white);
    font-weight: 700; font-size: 18px; letter-spacing: 0.6px; text-transform: uppercase;
  }
  .col-heads .col-name { width: 158px; text-align: left; padding-left: 12px; }
  .col-heads .col-details { text-align: center; }

  .competency-name {
    vertical-align: top; padding: 20px 12px 0; font-size: 17.5px; font-weight: 500;
  }
  .details { vertical-align: top; padding: 18px 14px 0 18px; }
  .details ul { list-style: none; }
  .details li {
    position: relative; padding-left: 28px; margin-bottom: 12px;
    font-size: 17px; font-weight: 500; line-height: 1.3;
  }
  .details li svg { position: absolute; left: 0; top: 3px; width: 16px; height: 16px; }

  .row-communicator { height: 130px; }
  .row-critical { height: 152px; }
  .row-responsible { height: 133px; }
  .row-adaptable { height: 157px; }
  .row-collaborator { height: 132px; }
  .row-compassionate { height: 152px; }

  .poster-footer {
    height: 82px; display: flex; align-items: center; gap: 22px;
    padding: 0 56px; background: var(--white); font-size: 18px; font-weight: 500;
  }
  .contact { display: flex; align-items: center; gap: 8px; }
  .contact svg { width: 26px; height: 26px; flex: none; }
  .contact-address { line-height: 1.3; font-size: 17.5px; }
  .contact-address strong { display: block; font-weight: 700; }
</style>
</head>
<body>
<svg width="0" height="0" style="position:absolute">
  <symbol id="tick" viewBox="0 0 16 16">
    <circle cx="8" cy="8" r="8" fill="#0e0f3d"/>
    <path d="M4.5 8.3l2.3 2.3 4.7-4.9" fill="none" stroke="#fff" stroke-width="1.9" stroke-linecap="round" stroke-linejoin="round"/>
  </symbol>
</svg>

<div class="poster">
  <main class="poster-main">
    <h1 class="poster-title">Profile of a Drifter</h1>
    <div class="district-mark"><span class="dot"></span>Corvath Falls</div>

    <table class="competency-table">
      <thead>
        <tr class="table-caption"><th colspan="2">Competency Suggestions</th></tr>
        <tr class="col-heads"><th class="col-name">Competency</th><th class="col-details">Details</th></tr>
      </thead>
      <tbody>
        <tr class="row-communicator">
          <td class="competency-name">Communicator</td>
          <td class="details"><ul>
            <li><svg><use href="#tick"/></svg>Expresses ideas clearly and respectfully (written &amp; verbal).</li>
            <li><svg><use href="#tick"/></svg>Listens actively and understands diverse perspectives.</li>
            <li><svg><use href="#tick"/></svg>Adjusts communication to suit the audience and context.</li>
          </ul></td>
        </tr>
        <tr class="row-critical">
          <td class="competency-name">Critical Thinker</td>
          <td class="details"><ul>
            <li><svg><use href="#tick"/></svg>Questions, analyzes, and evaluates information from multiple sources.</li>
            <li><svg><use href="#tick"/></svg>Identifies and solves complex problems creatively.</li>
            <li><svg><use href="#tick"/></svg>Uses evidence and diverse perspectives to form reasoned conclusions and make informed decisions.</li>
          </ul></td>
        </tr>
        <tr class="row-responsible">
          <td class="competency-name">Responsible</td>
          <td class="details"><ul>
            <li><svg><use href="#tick"/></svg>Takes ownership of actions, choices, and commitments.</li>
            <li><svg><use href="#tick"/></svg>Manages time, resources, and self to meet expectations.</li>
            <li><svg><use href="#tick"/></svg>Acts with integrity and advocates for self and others.</li>
          </ul></td>
        </tr>
        <tr class="row-adaptable">
          <td class="competency-name">Adaptable</td>
          <td class="details"><ul>
            <li><svg><use href="#tick"/></svg>Responds productively to new situations, challenges, and feedback.</li>
            <li><svg><use href="#tick"/></svg>Learns from new experiences &amp; applies prior knowledge in evolving contexts.</li>
            <li><svg><use href="#tick"/></svg>Adjusts behavior and approach to effectively engage with diverse groups and environments.</li>
          </ul></td>
        </tr>
        <tr class="row-collaborator">
          <td class="competency-name">Collaborator</td>
          <td class="details"><ul>
            <li><svg><use href="#tick"/></svg>Contributes effectively and cooperatively to shared goals.</li>
            <li><svg><use href="#tick"/></svg>Listens actively and values diverse ideas and perspectives.</li>
            <li><svg><use href="#tick"/></svg>Engages respectfully, compromising and leading when appropriate.</li>
          </ul></td>
        </tr>
        <tr class="row-compassionate">
          <td class="competency-name">Compassionate</td>
          <td class="details"><ul>
            <li><svg><use href="#tick"/></svg>Understands &amp; acknowledges others' feelings, perspectives, &amp; experiences.</li>
            <li><svg><use href="#tick"/></svg>Responds with kindness, patience, and support.</li>
            <li><svg><use href="#tick"/></svg>Seeks to connect with and contribute positively to the well-being of others and the community.</li>
          </ul></td>
        </tr>
      </tbody>
    </table>
  </main>

  <footer class="poster-footer">
    <div class="contact">
      <svg viewBox="0 0 26 26"><circle cx="13" cy="13" r="13" fill="#9c1c24"/><path d="M13 6.5a4.3 4.3 0 0 0-4.3 4.3c0 3.2 4.3 7.4 4.3 7.4s4.3-4.2 4.3-7.4A4.3 4.3 0 0 0 13 6.5z" fill="none" stroke="#fff" stroke-width="1.6"/><circle cx="13" cy="10.8" r="1.5" fill="#fff"/><path d="M8 19.5h10" stroke="#fff" stroke-width="1.6" stroke-linecap="round"/></svg>
      <div class="contact-address"><strong>Corvath Falls Public Schools</strong>48 North Mill St. Corvath Falls, MI 49900</div>
    </div>
    <div class="contact">
      <svg viewBox="0 0 26 26"><circle cx="13" cy="13" r="13" fill="#9c1c24"/><path d="M9.2 7.2l2 2.6-1.2 1.5c.8 1.8 2.2 3.3 4 4.2l1.5-1.2 2.6 2-1.3 2c-4.6-.4-8.6-4.4-9-9z" fill="#fff"/></svg>
      <span>555-014-8190</span>
    </div>
    <div class="contact">
      <svg viewBox="0 0 26 26"><circle cx="13" cy="13" r="13" fill="#9c1c24"/><rect x="9" y="6.5" width="8" height="4" fill="#fff"/><rect x="7" y="11" width="12" height="6" rx="1" fill="#fff"/><rect x="9" y="15" width="8" height="5" fill="#fff" stroke="#9c1c24" stroke-width="1"/></svg>
      <span>555-014-8195</span>
    </div>
    <div class="contact">
      <svg viewBox="0 0 26 26"><circle cx="13" cy="13" r="13" fill="#9c1c24"/><g fill="none" stroke="#fff" stroke-width="1.4"><circle cx="13" cy="13" r="7"/><ellipse cx="13" cy="13" rx="3" ry="7"/><path d="M6 13h14M7.5 9.5h11M7.5 16.5h11"/></g></svg>
      <span>corvath.k12.example.us</span>
    </div>
  </footer>
</div>
</body>
</html>
```